Business Card for Managing Partner Investment Fund

To create a business card template for an investment fund manager. Business card should be more professional in nature, not too colorful, more upscale, and created using the attached logos and fund name files. I would prefer a black or gray color scheme, but am open to the use of color as well. I would prefer a double sided business card, but open to single sided business card designs as well. The business card should include: name, title, and contact information, as well as logo and company name. I would prefer a more stream-lined, simple business card design.
Updates
Address: 4190 NE 38th Ter. Ocala, FL 34470
Email: talvin47@quorimail.net
Phone: 561-347-9162
Title: managing partner
Name: Dorian Velsky
Fund Name: Ambergate Capital
Logos can be found in files attached to the brief
Target Market(s)
potential investors, other fund managers
Industry/Entity Type
Finance
Contact Information for Business Card
Name on card: Dorian Velsky
Title: Managing Partner
Colors
Designer to choose colors to be used in the design.
Requirements
Must have
- Phone number
- email address
- physical address
- title
- name
- logo
- Fund name
Nice to have
- simple layout
Should not have
- too many colors, busy fonts,

```html
<!DOCTYPE html>
<html lang="en">
<head>
<meta charset="utf-8">
<title>Ambergate Capital – Business Card</title>
<link href="https://fonts.googleapis.com/css2?family=Roboto:wght@400&family=Roboto+Condensed:wght@400;500&display=swap" rel="stylesheet">
<style>
  :root {
    --backdrop: #232323;
    --card-dark: #5f5f5f;
    --card-light: #ececec;
    --snow: #ffffff;
    --ink-strong: #646464;
    --ink-soft: #8a8a8a;
    --shadow: rgba(0, 0, 0, 0.55);
  }
  * { margin: 0; padding: 0; box-sizing: border-box; }
  html, body {
    width: 1200px;
    height: 960px;
    overflow: hidden;
    background: var(--backdrop);
  }
  .canvas {
    position: relative;
    width: 1200px;
    height: 960px;
  }
  .card {
    position: absolute;
    width: 600px;
    height: 342px;
    overflow: hidden;
    box-shadow: 2px 3px 6px var(--shadow);
  }
  .card--front {
    left: 314px;
    top: 113px;
    background: var(--card-dark);
  }
  .card--back {
    left: 311px;
    top: 472px;
    background: var(--card-light);
  }
  .mountain-art {
    position: absolute;
    left: 0;
    right: 0;
    top: 150px;
    bottom: 0;
    background: linear-gradient(180deg, var(--card-dark) 0%, #bdbdbd 55%, #f2f2f2 100%);
  }
  .contact {
    position: absolute;
    left: 43px;
    top: 39px;
    font-family: "Roboto", Arial, sans-serif;
    font-size: 14px;
    line-height: 18px;
    color: var(--snow);
  }
  .contact__address { margin-bottom: 10px; }
  .contact__line {
    display: flex;
    align-items: center;
    gap: 8px;
    height: 19px;
  }
  .contact__icon {
    width: 13px;
    height: 13px;
    fill: var(--snow);
    flex: none;
  }
  .brand {
    position: absolute;
    left: 0;
    right: 0;
    top: 128px;
    text-align: center;
    font-family: "Roboto Condensed", Arial, sans-serif;
    font-weight: 500;
    font-size: 36px;
    letter-spacing: 2px;
    color: var(--ink-strong);
  }
  .holder {
    position: absolute;
    left: 0;
    right: 0;
    top: 249px;
    text-align: center;
    font-family: "Roboto Condensed", Arial, sans-serif;
  }
  .holder__name {
    font-size: 21px;
    font-weight: 500;
    color: var(--ink-strong);
    line-height: 26px;
  }
  .holder__title {
    font-size: 16px;
    font-weight: 400;
    color: var(--ink-soft);
    letter-spacing: 0.3px;
    line-height: 20px;
  }
</style>
</head>
<body>
<main class="canvas">
  <section class="card card--front">
    <div class="mountain-art" role="img" aria-label="Illustration of white snow-capped mountain peaks across the lower card"></div>
    <div class="contact">
      <p class="contact__address">4190 NE 38th Ter.<br>Ocala, FL 34470</p>
      <p class="contact__line">
        <svg class="contact__icon" viewBox="0 0 16 16" aria-hidden="true"><path d="M3.6 1.2l2.3 2.8-1.3 1.9c.9 2 2.5 3.6 4.5 4.5l1.9-1.3 2.8 2.3-1.2 2.3C7.4 15.2.8 8.6 1.3 2.4z"/></svg>
        <span>561-347-9162</span>
      </p>
      <p class="contact__line">
        <svg class="contact__icon" viewBox="0 0 16 16" aria-hidden="true"><path d="M1 3.5h14v9H1z M1.8 4.3L8 9l6.2-4.7" fill="none" stroke="#fff" stroke-width="1.4"/><path d="M1 3.5h14L8 8.6z"/></svg>
        <span>talvin47@quorimail.net</span>
      </p>
      <p class="contact__line">
        <svg class="contact__icon" viewBox="0 0 16 16" aria-hidden="true"><circle cx="8" cy="8" r="7"/><path d="M5 4.5c1.5.5 2 1.8 1.2 3S4.5 9 5.5 11M10 3.5c-.5 1.5.5 2.5 1.8 2.8M9.5 13c.3-1.5 1.5-2.5 3-2.5" fill="none" stroke="#5f5f5f" stroke-width="1.3"/></svg>
        <span>www.ambergatecap.net</span>
      </p>
    </div>
  </section>

  <section class="card card--back">
    <p class="brand">AMBERGATE CAPITAL</p>
    <div class="holder">
      <p class="holder__name">DORIAN VELSKY</p>
      <p class="holder__title">MANAGING PARTNER</p>
    </div>
  </section>
</main>
</body>
</html>
```